Kindle Book Cover for Teen Financial Niche

Had a temporary cover done for the book but it needs a lot better cover now it is starting to get some traction.
The current book can be seen here:
https://www.brindlepost.com/dp/Q7K42WZ9RT
I am wanting something very different if possible. Please search books in the teen financial niche on Brindlepost and you will see that a lot of the covers are very similar in style.
I am looking for something different that will stand out in a crowded marketplace.
If you are putting someone on the cover please use a male character rather than a female one.
Thanks
Tobin

```html
<!DOCTYPE html>
<html lang="en">
<head>
<meta charset="utf-8">
<title>Everyday Dollars for Teens and Young Adults — Book Cover</title>
<link href="https://fonts.googleapis.com/css2?family=Fontdiner+Swanky&family=Montserrat:wght@700&family=Titan+One&family=Lilita+One&family=Rye&display=swap" rel="stylesheet">
<style>
  :root {
    --paper: #f4f6fb;
    --rule: #b9cbeb;
    --navy: #1b4a8f;
    --white: #ffffff;
    --red: #f93535;
    --art-light: #eaf1e6;
    --art-mid: #cfe3c4;
    --art-warm: #f3d6cc;
  }
  html, body {
    margin: 0;
    padding: 0;
    width: 750px;
    height: 1200px;
    overflow: hidden;
  }
  .cover {
    position: relative;
    width: 750px;
    height: 1200px;
    background-color: var(--paper);
    background-image: repeating-linear-gradient(
      to bottom,
      transparent 0,
      transparent 31px,
      var(--rule) 31px,
      var(--rule) 33px,
      transparent 33px,
      transparent 56px
    );
    background-size: 750px 56px;
    overflow: hidden;
  }
  .author, .title, .subtitle {
    position: absolute;
    left: 0;
    top: 0;
  }
  .author text {
    font-family: "Montserrat", sans-serif;
    font-weight: 700;
    font-size: 58px;
    fill: var(--navy);
  }
  .illustration {
    position: absolute;
    left: 55px;
    top: 112px;
    width: 650px;
    height: 520px;
    border-radius: 40px;
    background: radial-gradient(ellipse at 50% 55%, var(--art-warm) 0%, var(--art-mid) 55%, var(--art-light) 100%);
  }
  .title text {
    font-family: "Titan One", sans-serif;
    font-size: 132px;
    fill: var(--white);
    stroke: var(--navy);
    stroke-width: 22px;
    stroke-linejoin: round;
    paint-order: stroke fill;
  }
  .audience-band {
    position: absolute;
    left: 0;
    top: 903px;
    width: 750px;
    height: 77px;
    background: var(--red);
    display: flex;
    align-items: center;
    justify-content: center;
  }
  .audience {
    margin: 0;
    font-family: "Fontdiner Swanky", "Rye", cursive;
    font-size: 36px;
    color: var(--white);
    letter-spacing: 1px;
    white-space: nowrap;
  }
  .subtitle text {
    font-family: "Lilita One", sans-serif;
    font-size: 36px;
    fill: var(--navy);
  }
</style>
</head>
<body>
<main class="cover">
  <svg class="author" width="750" height="110" viewBox="0 0 750 110" aria-label="Elias Marden">
    <text x="47" y="82" textLength="652" lengthAdjust="spacing">ELIAS MARDEN</text>
  </svg>

  <div class="illustration" role="img" aria-label="Cartoon illustration of two smiling teenagers holding stacks of green banknotes, with bills floating around them"></div>

  <svg class="title" width="750" height="900" viewBox="0 0 750 900">
    <text x="42" y="755" textLength="666" lengthAdjust="spacingAndGlyphs">EVERYDAY</text>
    <text x="106" y="873" textLength="528" lengthAdjust="spacingAndGlyphs">DOLLARS</text>
  </svg>

  <div class="audience-band">
    <p class="audience">FOR TEENS AND YOUNG ADULTS</p>
  </div>

  <svg class="subtitle" width="750" height="1200" viewBox="0 0 750 1200" aria-label="Cash Confidence: A Simple Guide to Making Money, Smart Shopping, Planning Ahead and Growing It">
    <text x="85" y="1036" textLength="580" lengthAdjust="spacingAndGlyphs">CASH CONFIDENCE: A SIMPLE GUIDE TO</text>
    <text x="83" y="1084" textLength="584" lengthAdjust="spacingAndGlyphs">MAKING MONEY, SMART SHOPPING,</text>
    <text x="64" y="1132" textLength="622" lengthAdjust="spacingAndGlyphs">PLANNING AHEAD AND GROWING IT</text>
  </svg>
</main>
</body>
</html>
```